High quality health product needs a label

If you are a top professional designer for exclusive product labels, please read on.

High quality health products are being filled into so called Talvo glass bottles (see attachment) and I want to create labels for a range of different herbs (i.e. teasel, artemesia annua) in various dosage forms (i.e. liquid, capsules and tea). The brand of these products is called quellona.

The label for each type of herb shall have a small variance in color, i.e. teasel can have some violet and artemesia annua a green theme. The variance in color should be unique (not just 2 circles and a triangle) and abstract (i.e. no leafs). Please have a look at 2 of our labels we have created for other products.

The logo I feel comfortable with is attached in the file pixelgrove. I only want to take the leaf as logo, nothing else. The color of the logo should be adapted to our needs, but a green leaf makes sense to me. The color of the logo does not change for the variations of the label.

What do I expect in terms of design:

- minimalistic
- exclusive
- luxury
- classy
- abstract
- playful
- uniqueness

The front of the label should show:
- logo
- name of the herb, i.e. teasel
- dosage form, i.e. extract
- content, i.e. 250 ml
- the 2 logos to indicate that the product is certified organic

The back will contain some basic information that I will provide once I selected your design.

The final deliverables are 4 illustrator (compatible with version 16) ai vector files for 4 different types of herbs. Once the initial design is set, we need to create 3 color variations.

Please use a 100 mm x 210 mm layout for the 500 ml syrup bottle.

Target Market(s)

people with an interest in their health

Industry/Entity Type

health

Font styles to use
Sans Serif

Requirements
Must have
• abstract, unique, luxury, high class, minimalistic
Should not have
• overloaded, too many colors,

```html
<!DOCTYPE html>
<html lang="en">
<head>
<meta charset="utf-8">
<title>Teasel Extract – Label</title>
<link rel="stylesheet" href="https://fonts.googleapis.com/css2?family=Montserrat:wght@300;400;700&display=swap">
<style>
  :root {
    --page: #ffffff;
    --label-bg: #ffffff;
    --frame: #1a1a1a;
    --brand-green: #1f5e2a;
    --violet-deep: #7a4ee6;
    --violet-mid: #9a78f0;
    --violet-soft: #d3c4fa;
    --type-light: #ffffff;
    --ink: #3a3a3a;
    --badge-red: #c0392b;
    --badge-green: #7cb82f;
  }
  * { margin: 0; padding: 0; box-sizing: border-box; }
  html, body {
    width: 1200px; height: 1200px; overflow: hidden;
    background: var(--page);
    font-family: "Montserrat", sans-serif;
  }
  .label {
    position: absolute;
    left: 50px; top: 338px;
    width: 1100px; height: 524px;
    background: var(--label-bg);
    border: 2px solid var(--frame);
  }
  .brand {
    position: absolute;
    left: 0; right: 0; top: 64px;
    text-align: center;
    color: var(--brand-green);
    font-weight: 700;
    font-size: 28px;
    letter-spacing: 0.42em;
    padding-left: 0.42em;
  }
  .color-field {
    position: absolute;
    left: 351px; top: 150px;
    width: 400px; height: 270px;
    background: linear-gradient(180deg,
      var(--violet-soft) 0%,
      var(--violet-mid) 14%,
      var(--violet-deep) 40%,
      var(--violet-mid) 70%,
      var(--violet-soft) 100%);
    border-radius: 22px 30px 18px 26px / 34px 24px 30px 20px;
  }
  .herb-name {
    position: absolute;
    left: 351px; width: 400px; top: 218px;
    text-align: center;
    color: var(--type-light);
    font-weight: 400;
    font-size: 60px;
    line-height: 1;
    letter-spacing: 0.16em;
    padding-left: 0.16em;
  }
  .divider {
    position: absolute;
    left: 435px; top: 290px;
    width: 232px; height: 2px;
    background: var(--type-light);
  }
  .dosage-form {
    position: absolute;
    left: 351px; width: 400px; top: 302px;
    text-align: center;
    color: var(--type-light);
    font-weight: 300;
    font-size: 44px;
    line-height: 1;
    letter-spacing: 0.08em;
  }
  .volume {
    position: absolute;
    left: 0; right: 0; top: 470px;
    text-align: center;
    color: var(--ink);
    font-weight: 300;
    font-size: 23px;
  }
  .cert-badges {
    position: absolute;
    left: 694px; top: 440px;
  }
</style>
</head>
<body>
  <main class="label">
    <div class="brand">QUELLONA</div>

    <div class="color-field" role="img" aria-label="Violet watercolour wash behind the product name"></div>
    <h1 class="herb-name">TEASEL</h1>
    <div class="divider"></div>
    <h2 class="dosage-form">Extract</h2>

    <p class="volume">250 ml</p>

    <svg class="cert-badges" width="44" height="74" viewBox="0 0 44 74" aria-label="Organic certification badges">
      <circle cx="22" cy="18" r="16" fill="#ffffff" stroke="var(--badge-red)" stroke-width="2"/>
      <rect x="1" y="42" width="42" height="30" fill="var(--badge-green)"/>
    </svg>
  </main>
</body>
</html>
```